Redesign of Stillwater Grove website

- I would like to redesign my ministry website (vostel.org)
- Re-brand it with my new logo.

I am looking for something professional and artistic, and focused on creating a good user experience.

The purpose of the site is to:
- Expose VOSTEL to the world
- Inform the public about what we are all about.
- Promote my publications (https://www.bookshelfexample.test/Quiet-Pilgrim-Leaving-Patterned-Paths-ebook/dp/Q7ZX42KT9W/ref=dp_kinw_strp_1)

I don't have to many media material, so I am open to suggestions if the provided images will enhance the look and feel of the site.

Target Market(s)

All English speaking christians , and aspiring Christians around the world.

Industry/Entity Type

Religious

Number of Pages Required

3 page

Font styles to use
Sans Serif

Requirements
Must have
• - Add donation link through CoinBridge
• - A mission page that contains the description found on the "About us" page on Vostel.org
• - A personal author page that will include my bio, publication, and contact information. People should be able to email me right from the page
• - Social media links
Nice to have
• - An address book, were people can send us their contact information.

```html
<!DOCTYPE html>
<html lang="en">
<head>
<meta charset="utf-8">
<title>VOSTEL – Ministry</title>
<link href="https://fonts.googleapis.com/css2?family=Noto+Serif:wght@400&family=Arimo:wght@400;700&family=Roboto:wght@300;400;500&family=Cinzel:wght@600&display=swap" rel="stylesheet">
<style>
:root{
  --orange:#f7941d;
  --navy:#0f3a5f;
  --navy-deep:#0c3358;
  --ink:#222;
  --footer:#23272b;
  --bottom:#15171a;
  --rule:#3a3f45;
}
*{margin:0;padding:0;box-sizing:border-box}
html,body{width:1108px;height:1200px;overflow:hidden;background:#fff}
body{position:relative;font-family:"Roboto",sans-serif;color:var(--ink)}
.abs{position:absolute}

/* header */
.contact-line{left:94px;top:14px;font:400 12px "Noto Serif",serif;color:#333}
.donate-btn{left:91px;top:61px;width:99px;height:27px;background:var(--navy);display:flex;align-items:center;gap:5px;padding-left:6px;color:#fff;font:400 17px "Noto Serif",serif}
.donate-btn .dot{width:17px;height:17px;border-radius:50%;background:var(--orange)}
.brand{left:454px;top:50px;width:222px;text-align:center}
.brand-name{font:600 46px "Cinzel",serif;color:var(--navy);letter-spacing:1px;line-height:1}
.social{display:flex;gap:11px}
.social span{width:29px;height:29px;border-radius:50%;background:#e7e7e7;display:flex;align-items:center;justify-content:center;font:500 10px "Roboto",sans-serif;color:#333}
.social.top{left:830px;top:55px}

/* nav */
.nav-rule{left:0;top:120px;width:1108px;height:1px;background:#e3e3e3}
.main-nav{left:0;top:121px;width:1108px;height:58px;font:400 12.5px "Noto Serif",serif;color:#222}
.main-nav a{position:absolute;top:22px;color:inherit;text-decoration:none}
.main-nav .active::before{content:"";position:absolute;left:1px;top:-12px;width:7px;height:9px;background:var(--orange);border-radius:50%}

/* hero */
.hero{left:0;top:179px;width:1108px;height:429px;background:radial-gradient(ellipse at 62% 75%,#5a3a1e 0%,#2a1a0e 45%,#0d0906 100%)}
.cover{left:90px;top:211px;width:231px;height:396px;background:linear-gradient(180deg,#3a3a3a 0%,#6e6a62 40%,#8a7560 75%,#6b5440 100%)}
.book-label{left:381px;top:240px;font:400 36px "Noto Serif",serif;color:#fff}
.credits{right:91px;top:245px;font:400 17px "Roboto",sans-serif;color:#fff;line-height:25px}
.credits b{font-weight:400;color:var(--orange);display:inline-block;width:65px}
.hero-rule{left:381px;top:298px;width:636px;height:1px;background:#8a7a6a}
.book-title{left:382px;top:322px;font:400 45px "Arimo",sans-serif;color:var(--orange);letter-spacing:0.5px}
.book-sub{left:390px;top:372px;font:300 24px "Roboto",sans-serif;color:#ddd}
.price{top:430px;height:48px;border:1px solid var(--orange);display:flex;align-items:center;gap:14px;padding-left:10px;color:#fff;font:300 23px "Roboto",sans-serif}
.price em{font:500 14px "Roboto",sans-serif;font-style:normal;color:var(--orange)}
.checkout{left:386px;top:515px;width:195px;height:48px;background:var(--orange);border-radius:4px;display:flex;align-items:center;justify-content:center;color:#fff;font:500 15px "Roboto",sans-serif;text-decoration:none}

/* quote */
.scripture{left:0;top:635px;width:1108px;text-align:center;font:400 19.5px/28px "Arimo",sans-serif;color:var(--orange)}
.scripture cite{display:block;margin-top:12px;font-style:normal;color:var(--navy)}

/* ministries band */
.band{left:0;top:787px;width:1108px;height:110px;background:var(--navy-deep)}
.ministry{top:0;height:110px;display:flex;align-items:center;gap:16px;color:#fff;font:400 21px "Roboto",sans-serif}
.ministry .badge{width:46px;height:46px;border-radius:8px;background:var(--orange)}

/* footer */
.footer{left:0;top:897px;width:1108px;height:255px;background:var(--footer)}
.col{top:945px}
.col h3{font:500 17px "Roboto",sans-serif;color:#fff;padding-bottom:8px;border-bottom:1px solid #4a4f55;position:relative}
.col h3 span{color:var(--orange)}
.col h3::after{content:"";position:absolute;left:0;bottom:-2px;width:33px;height:3px;background:var(--orange)}
.vrule{top:948px;width:1px;height:170px;background:var(--rule)}
.links{display:grid;grid-template-columns:95px 80px;row-gap:8px;margin-top:14px;font:300 12px "Roboto",sans-serif;color:#ccc;list-style:none;grid-auto-flow:column;grid-template-rows:repeat(6,16px)}
.links li::before{content:"›";margin-right:5px}
.links .on{color:var(--orange)}
.col p{font:300 12.5px/18px "Roboto",sans-serif;color:#ddd}
.field{background:#fff;font:300 12.5px "Roboto",sans-serif;color:#555;display:flex;align-items:center;padding-left:10px}
.btn{background:var(--orange);color:#fff;font:700 14px "Arimo",sans-serif;display:flex;align-items:center;justify-content:center}
.info{font:300 12.5px/18px "Roboto",sans-serif;color:#ccc;display:flex;align-items:center;gap:8px}

/* bottom bar */
.bottom{left:0;top:1152px;width:1108px;height:48px;background:var(--bottom)}
.copyright{left:91px;top:1169px;font:300 12px "Roboto",sans-serif;color:#ddd}
.payment{left:493px;top:1156px;width:123px;height:40px;border:2px solid #1e4a8a;background:#fff;display:flex;align-items:center;justify-content:center;gap:5px;font:700 13px "Arimo",sans-serif;color:var(--navy)}
.payment i{width:8px;height:8px;background:var(--navy);display:block}
.social.bottom-icons{left:830px;top:1162px}
</style>
</head>
<body>

<header>
  <div class="abs contact-line">Write me: hello@vostel.org</div>
  <a class="abs donate-btn"><span class="dot"></span>Donate</a>
  <div class="abs brand"><div class="brand-name">VOSTEL</div></div>
  <div class="abs social top" aria-label="Social links">
    <span>Fr</span><span>Ch</span><span>Lw</span><span>Cs</span><span>Vt</span>
  </div>
</header>

<div class="abs nav-rule"></div>
<nav class="abs main-nav">
  <a class="active" style="left:169px">Home</a>
  <a style="left:279px">About Us</a>
  <a style="left:409px">Events</a>
  <a style="left:523px">Mission</a>
  <a style="left:643px">Partners</a>
  <a style="left:769px;top:20px">Support</a>
  <a style="left:891px;top:20px">Contact Us</a>
</nav>

<section class="abs hero" role="img" aria-label="Dimly lit open book on a table"></section>
<div class="abs cover" role="img" aria-label="Book cover: a lone traveller on a rainy dirt road under a stormy sky"></div>
<h2 class="abs book-label">My Book</h2>
<div class="abs credits">
  <div><b>Author :</b>Elias Marrow Tenley</div>
  <div><b>Editor :</b>Ruth Calloway</div>
</div>
<div class="abs hero-rule"></div>
<h1 class="abs book-title">THE QUIET PILGRIM</h1>
<div class="abs book-sub">Leaving Patterned Paths</div>
<div class="abs price" style="left:386px;width:143px"><em>E-book</em>$8.87</div>
<div class="abs price" style="left:550px;width:174px"><em>Hardcover</em>$16.99</div>
<div class="abs price" style="left:746px;width:166px"><em>Paperback</em>$8.87</div>
<a class="abs checkout">Checkout with Bookshelf</a>

<blockquote class="abs scripture">
  Go your way, Daniel, for the words are closed up and sealed till the time of the end.<br>
  Many shall be purified, made white, and refined, but the wicked shall do wickedly; and<br>
  none of the wicked shall understand, but the wise shall understand.
  <cite>Daniel 12:9-10</cite>
</blockquote>

<section class="abs band">
  <div class="abs ministry" style="left:90px"><span class="badge" role="img" aria-label="Sunday service icon"></span><span>Sunday Service</span></div>
  <div class="abs ministry" style="left:376px"><span class="badge" role="img" aria-label="Prayer icon"></span><span>Prayer</span></div>
  <div class="abs ministry" style="left:555px"><span class="badge" role="img" aria-label="Prophetic season icon"></span><span>Prophetic Season</span></div>
  <div class="abs ministry" style="left:828px"><span class="badge" role="img" aria-label="Events calendar icon"></span><span>Latest Events</span></div>
</section>

<footer class="abs footer"></footer>
<div class="abs vrule" style="left:288px"></div>
<div class="abs vrule" style="left:563px"></div>
<div class="abs vrule" style="left:789px"></div>

<div class="abs col" style="left:90px;width:175px">
  <h3><span>Quick</span> Links</h3>
  <ul class="links">
    <li class="on">Home</li><li>About Us</li><li>Events</li><li>Mission</li><li>Partners</li><li>Donate</li>
    <li>Support</li><li>Contact Us</li>
  </ul>
</div>

<div class="abs col" style="left:320px;width:215px">
  <h3><span>Newsletter</span> Signup</h3>
  <p style="margin-top:14px">Ut wisi enim ad minim veniam,dollarm Mor nostrni.</p>
  <div class="field" style="width:215px;height:36px;margin-top:12px;padding-left:15px">Enter your email here</div>
  <div class="btn" style="width:120px;height:36px;margin-top:17px">SUBSCRIBE</div>
</div>

<div class="abs col" style="left:593px;width:170px">
  <h3><span>Contact</span> Details</h3>
  <p style="margin-top:12px;font-weight:400;font-size:14px;color:#eee">STILLWATER GROVE</p>
  <p style="color:#ccc">80 Alder road Brookfield,<br>Maine 04400, USA</p>
  <div class="info" style="margin-top:9px">
    <svg width="12" height="12" viewBox="0 0 12 12"><path d="M2 1 L4 1 L5 4 L3.5 5 Q5 8 7 8.5 L8 7 L11 8 L11 10 Q10 11 8 11 Q1 9 1 2 Z" fill="#ccc"/></svg>(555) 0142 3380</div>
  <div class="info" style="margin-top:9px">
    <svg width="12" height="12" viewBox="0 0 12 12"><rect x="3" y="1" width="6" height="3" fill="#ccc"/><rect x="1" y="4" width="10" height="5" rx="1" fill="#ccc"/><rect x="3" y="8" width="6" height="3" fill="#fff"/></svg>(555) 0142 3380</div>
  <div class="info" style="margin-top:9px">
    <svg width="12" height="10" viewBox="0 0 12 10"><rect x="0.5" y="1" width="11" height="8" fill="#ccc"/><path d="M0.5 1 L6 6 L11.5 1" stroke="#23272b" fill="none"/></svg>info@vostel.org</div>
</div>

<div class="abs col" style="left:819px;width:199px">
  <h3><span>Quick</span> Contact</h3>
  <div class="field" style="width:199px;height:32px;margin-top:14px">Name</div>
  <div class="field" style="width:199px;height:32px;margin-top:6px">Email</div>
  <div class="field" style="width:199px;height:32px;margin-top:6px">Message</div>
  <div class="btn" style="width:111px;height:32px;margin-top:7px">SUBMIT</div>
</div>

<div class="abs bottom"></div>
<div class="abs copyright">Copyright © 2016 VOSTEL. All Rights Reserved.</div>
<div class="abs payment"><i></i>CoinBridge</div>
<div class="abs social bottom-icons" aria-label="Social links">
  <span>Fr</span><span>Ch</span><span>Lw</span><span>Cs</span><span>Vt</span>
</div>

</body>
</html>
```